Website for The Copper Lantern

We need an impressive e-commerce website for our newly launched business "The Copper Lantern".
The Copper Lantern searches store-front and online retailers for diamond engagement rings according to the client's specified requirements. We want to save people time by doing the shopping around for them.
We can relate to, and we love, www.roomtrellis.com
Like roomtrellis.com, we want to offer website visitors a quick run-down on how the process works, then offer them to elect a service package and pay for that package on the spot.
Content pages:
HOME
HOW IT WORKS
DIAMOND GALLERY
ABOUT
FAQs
CONTACT
Inclusions: Our logo and Facebook and Instagram buttons
We want to be able to easily edit this website, We want it to display well on iPhone and android, We want it to be clean and striking.
Like our logo, we want our website to embody elegant masculinity.
Target Market(s)
Men in market for diamond ring purchase $5k - $50k
Industry/Entity Type
Business
Number of Pages Required
5+ page
Font styles to use
Look and feel

```html
<!DOCTYPE html>
<html lang="en">
<head>
<meta charset="utf-8">
<title>The Copper Lantern — Shop</title>
<link href="https://fonts.googleapis.com/css2?family=Lato:wght@400;700&family=Oswald:wght@500&display=swap" rel="stylesheet">
<style>
:root{
  --ink:#333;
  --muted:#666;
  --line:#d9d9d9;
  --nav:#5b5b5b;
  --hero-top:#8c8c8c;
  --hero-bottom:#6e6e6e;
  --crumb:#b7b7b7;
  --photo:#bcbcbc;
  --badge:#4a4a4a;
  --footer:#232323;
  --footer-base:#121212;
  --footer-text:#d6d6d6;
  --white:#fff;
}
*{box-sizing:border-box;margin:0;padding:0}
html,body{width:771px;height:1200px;overflow:hidden}
body{position:relative;background:var(--white);font-family:"Lato",Arial,sans-serif;color:var(--ink)}
.top-rule{height:4px;background:#444}

.site-header{position:relative;height:118px}
.header-contact{position:absolute;left:104px;top:56px;font-size:8px;color:var(--muted);display:flex;align-items:center;gap:4px}
.header-contact svg{width:7px;height:7px}
.header-account{position:absolute;right:104px;top:56px;font-size:8px;color:var(--muted);display:flex;align-items:center;gap:4px}
.header-account svg{width:8px;height:8px}
.brand{position:absolute;left:0;right:0;top:26px;text-align:center;color:#555}
.brand-mark{width:22px;height:22px;border-radius:50%;border:2px solid #777;margin:0 auto 8px}
.brand-name{font-size:11px;letter-spacing:1.5px;text-transform:uppercase;line-height:1.35;font-weight:400}

.main-nav{height:26px;background:var(--nav);position:relative}
.main-nav a{position:absolute;top:8px;transform:translateX(-50%);font-size:8px;color:var(--white);text-decoration:none;text-transform:uppercase;letter-spacing:.3px}

.page-hero{height:119px;background:linear-gradient(var(--hero-top),var(--hero-bottom));display:flex;align-items:center;justify-content:center}
.page-hero h1{font-family:"Oswald",Arial,sans-serif;font-weight:500;color:var(--white);font-size:30px;letter-spacing:.5px;margin-top:-4px}

.breadcrumb{height:26px;background:var(--crumb);font-size:7px;font-weight:700;color:#555;padding:10px 0 0 104px}

.product-grid{position:absolute;left:104px;top:342px;display:grid;grid-template-columns:repeat(4,130px);column-gap:14.3px;row-gap:24px}
.product-card{width:130px;height:182px;border:1px solid var(--line);background:var(--white);position:relative;text-align:center}
.product-photo{position:absolute;left:9px;top:9px;width:111px;height:141px;background:radial-gradient(circle at 50% 55%,#e4e4e4 0,#c4c4c4 45%,var(--photo) 75%)}
.badge-new{position:absolute;right:9px;top:9px;background:var(--badge);color:var(--white);font-size:7px;font-weight:700;padding:2px 5px}
.product-actions{position:absolute;left:9px;top:130px;width:111px;height:20px;background:#3a3a3a;display:flex;justify-content:space-evenly;align-items:center}
.product-actions svg{width:10px;height:10px}
.product-name{position:absolute;left:0;right:0;top:157px;font-size:7.5px;color:#555}
.product-price{position:absolute;left:0;right:0;top:168px;font-size:8px;color:#444}

.load-more{position:absolute;left:348px;top:961px;width:75px;height:19px;background:#9a9a9a;color:var(--white);font-size:8.5px;font-weight:700;display:flex;align-items:center;justify-content:center;gap:4px}
.load-more svg{width:8px;height:8px}

.site-footer{position:absolute;left:0;top:1004px;width:771px;height:168px;background:var(--footer);color:var(--footer-text);font-size:7px;line-height:11.2px}
.footer-about{position:absolute;left:104px;top:30px;width:180px;text-align:justify}
.footer-about p+p{margin-top:11px}
.footer-links{position:absolute;left:297px;top:30px;list-style:none}
.footer-info{position:absolute;left:379px;top:30px;width:180px}
.footer-info h2{font-size:9px;font-weight:700;letter-spacing:.3px;margin-bottom:6px;color:#cfcfcf}
.footer-info p{color:#aaa}
.footer-info span{color:var(--footer-text)}
.payment-box{position:absolute;left:573px;top:37px;width:94px;height:24px;border:1px solid #ccc;border-radius:2px;display:flex;align-items:center;justify-content:center;gap:3px;padding-top:6px}
.payment-box i{display:block;width:19px;height:11px;background:#e9e9e9;border-radius:1px}
.social-list{position:absolute;left:573px;top:73px;display:flex;gap:6.5px;list-style:none}
.social-list li{width:18px;height:18px;background:#5e5e5e}

.footer-base{position:absolute;left:0;top:1172px;width:771px;height:28px;background:var(--footer-base);color:#ddd;font-size:7px;text-align:center;padding-top:10px}
.footer-base u{color:#bbb}
</style>
</head>
<body>
<div class="top-rule"></div>

<header class="site-header">
  <div class="header-contact">$ ▾ &nbsp;|&nbsp;
    <svg viewBox="0 0 10 10"><path d="M2 1l2 2-1 1.5c.6 1.2 1.3 1.9 2.5 2.5L7 6l2 2-1.5 1.5C4 9 1 6 .5 2.5z" fill="#666"/></svg>
    888-555-0147</div>
  <div class="brand">
    <div class="brand-mark"></div>
    <div class="brand-name">The<br>Copper Lantern</div>
  </div>
  <div class="header-account">Wish List (0) &nbsp;|
    <svg viewBox="0 0 10 10"><circle cx="4" cy="4" r="3" fill="none" stroke="#666" stroke-width="1.4"/><path d="M6 6l3 3" stroke="#666" stroke-width="1.4"/></svg>
    <svg viewBox="0 0 10 10"><circle cx="5" cy="3" r="2.3" fill="#666"/><path d="M1 10c0-3 2-4.5 4-4.5s4 1.5 4 4.5z" fill="#666"/></svg>
    <svg viewBox="0 0 10 10"><path d="M0 1h2l1.5 5h5L10 3H3" fill="none" stroke="#666" stroke-width="1.2"/><circle cx="4" cy="8.5" r="1" fill="#666"/><circle cx="8" cy="8.5" r="1" fill="#666"/></svg>
  </div>
</header>

<nav class="main-nav">
  <a href="#" style="left:182px">Home</a>
  <a href="#" style="left:251px">About Us</a>
  <a href="#" style="left:337px">How It Works</a>
  <a href="#" style="left:434px">Diamond Gallery</a>
  <a href="#" style="left:517px">Faqs</a>
  <a href="#" style="left:582px">Contact</a>
</nav>

<section class="page-hero"><h1>SHOP</h1></section>
<div class="breadcrumb">Home » Shop</div>

<main class="product-grid">
  <article class="product-card">
    <div class="product-photo" role="img" aria-label="Silver ring with square-set diamond"></div>
    <span class="badge-new">NEW!</span>
    <div class="product-actions">
      <svg viewBox="0 0 10 10"><path d="M0 1h2l1.5 5h5L10 3H3" fill="none" stroke="#fff" stroke-width="1.3"/><circle cx="4" cy="8.5" r="1" fill="#fff"/><circle cx="8" cy="8.5" r="1" fill="#fff"/></svg>
      <svg viewBox="0 0 10 10"><path d="M5 9L1.2 5.2A2.2 2.2 0 0 1 5 2.2a2.2 2.2 0 0 1 3.8 3z" fill="none" stroke="#fff" stroke-width="1.2"/></svg>
      <svg viewBox="0 0 10 10"><path d="M8.5 4A3.6 3.6 0 0 0 2 3M1.5 6A3.6 3.6 0 0 0 8 7" fill="none" stroke="#fff" stroke-width="1.3"/><path d="M2 .8v2.6h2.6M8 9.2V6.6H5.4" fill="none" stroke="#fff" stroke-width="1.2"/></svg>
    </div>
    <p class="product-name">Regal Stone</p><p class="product-price">$56.00</p>
  </article>
  <article class="product-card">
    <div class="product-photo" role="img" aria-label="Silver ring with diamond and side accents"></div>
    <p class="product-name">Regal Stone</p><p class="product-price">$102.00</p>
  </article>
  <article class="product-card">
    <div class="product-photo" role="img" aria-label="Wide silver ring with pavé diamond setting"></div>
    <span class="badge-new">NEW!</span>
    <p class="product-name">Regal Stone</p><p class="product-price">$102.00</p>
  </article>
  <article class="product-card">
    <div class="product-photo" role="img" aria-label="Silver band with channel-set diamonds"></div>
    <p class="product-name">Regal Stone</p><p class="product-price">$155.00</p>
  </article>

  <article class="product-card">
    <div class="product-photo" role="img" aria-label="Silver ring with square-set diamond"></div>
    <span class="badge-new">NEW!</span>
    <p class="product-name">Regal Stone</p><p class="product-price">$56.00</p>
  </article>
  <article class="product-card">
    <div class="product-photo" role="img" aria-label="Silver ring with diamond and side accents"></div>
    <p class="product-name">Regal Stone</p><p class="product-price">$102.00</p>
  </article>
  <article class="product-card">
    <div class="product-photo" role="img" aria-label="Wide silver ring with pavé diamond setting"></div>
    <span class="badge-new">NEW!</span>
    <p class="product-name">Regal Stone</p><p class="product-price">$102.00</p>
  </article>
  <article class="product-card">
    <div class="product-photo" role="img" aria-label="Silver band with channel-set diamonds"></div>
    <p class="product-name">Regal Stone</p><p class="product-price">$155.00</p>
  </article>

  <article class="product-card">
    <div class="product-photo" role="img" aria-label="Silver ring with square-set diamond"></div>
    <span class="badge-new">NEW!</span>
    <p class="product-name">Regal Stone</p><p class="product-price">$56.00</p>
  </article>
  <article class="product-card">
    <div class="product-photo" role="img" aria-label="Silver ring with diamond and side accents"></div>
    <p class="product-name">Regal Stone</p><p class="product-price">$102.00</p>
  </article>
  <article class="product-card">
    <div class="product-photo" role="img" aria-label="Wide silver ring with pavé diamond setting"></div>
    <span class="badge-new">NEW!</span>
    <p class="product-name">Regal Stone</p><p class="product-price">$102.00</p>
  </article>
  <article class="product-card">
    <div class="product-photo" role="img" aria-label="Silver band with channel-set diamonds"></div>
    <p class="product-name">Regal Stone</p><p class="product-price">$155.00</p>
  </article>
</main>

<div class="load-more">
  <svg viewBox="0 0 10 10"><path d="M8.5 4A3.6 3.6 0 0 0 2 3M1.5 6A3.6 3.6 0 0 0 8 7" fill="none" stroke="#fff" stroke-width="1.4"/><path d="M2 .8v2.6h2.6M8 9.2V6.6H5.4" fill="none" stroke="#fff" stroke-width="1.3"/></svg>
  Load More
</div>

<footer class="site-footer">
  <div class="footer-about">
    <p>Lorem ipsum dolor sit amet, consectetur adipiscing elit. Integer gravida nisl sed sapien placerat imperdiet. Aenean id est vel orci tempor dignissim. Ut ac est velit. Aliquam lorem nulla.</p>
    <p>Aliquam placerat ultrices libero, vel hendrerit orci bibendum vitae. Donec sit amet ex sollicitudin metus tincidunt convallis at vel nunc.</p>
  </div>
  <ul class="footer-links">
    <li>Home</li><li>About Us</li><li>How It Works</li><li>Diamond Gallery</li><li>Faqs</li><li>Contact</li><li>Delivery Information</li><li>Privacy Policy</li><li>Terms &amp; Conditions</li>
  </ul>
  <div class="footer-info">
    <h2>INFO CONTACT</h2>
    <p>Address: <span>CopperLantern, 18 Wren Lane 54321 Lyon France</span></p>
    <p>Telephone: <span>0100-555-246</span></p>
    <p>Email: <span>sales@copperlantern.com</span></p>
  </div>
  <div class="payment-box" aria-label="Accepted payment methods"><i></i><i></i><i></i><i></i></div>
  <ul class="social-list" aria-label="Social links"><li></li><li></li><li></li><li></li></ul>
</footer>
<div class="footer-base">Copyright 2016 <u>CopperLantern</u>. All Rights Reserved.</div>
</body>
</html>
```